Etikettendesign für Ergänzungsfuttermittel für Hunde
Zielgruppe
Ich bin Tierphysiotherapeutin und möchte ein Ergänzungsfuttermittel für Hunde erstellen und verkaufen. Dazu benötige ich ein passendes Etikett.
Aufgabenstellung
Das Ergänzungsfuttermittel ist ein Nährstoffpulver zur Unterstützung des Bewegungsapparats. Das soll bitte auch drauf stehen. Des weiteren sind 100% natürliche Inhaltsstoffe drin (Brennessel, Kurkuma, Leinsamen, Hagebutte, Löwenzahn). Es sollte erkennlich sein dass es für Hunde ist. Mein Firmenname ist Anka's Pfotenwerk. Dieser sollte ebenfalls auf dem Etikett stehen. Ich bin mir noch unschlüssig, ob mein Logo mit rauf passt oder nicht. Eine Wiedererkennung sollte gegeben sein. Soll aber nicht zu sehr auffallen. Das Wort 'Bewegungsapparat' sollte jedoch rausstechen. Die Farben sollten nicht zu knallig sein. Ruhige Töne und auf einander abgestimmt. Ich lasse mich überraschen und bedanke mich im Voraus! ♡ Die Maße der Verpackung sind anbei. Es wäre toll, wenn das Etikett einmal komplett rumgeht.
Auf der Rückseite:
Ergänzungsfuttermittel für Hunde
• trägt einer gesunden Gelenkfunktion bei
• zur Unterstützung des gesamten Bewegungsapparats
• für mehr Vitalität und Wohlbefinden
Zusammensetzung: Brennessel, Kurkuma, Hagebutten, Leinsamen, Löwenzahn
Analytische Bestandteile: Rohfaser 2,55%, Feuchtgehalt 12%
Fütterungsempfehlung:
Hunde bis 20kg - 1gr täglich (reicht für 6 Monate)
Hunde ab 20kg - 2gr täglich (reicht für 3 Monate)
Das Pulver kann unter dem Futter gemischt werden.
Nettomasse: 200g
Hinweis: kühl, trocken und lichtgeschützt lagern.

```html
<!DOCTYPE html>
<html lang="de">
<head>
<meta charset="utf-8">
<title>Nährstoffpulver Etikett – Anka's Pfotenwerk</title>
<link href="https://fonts.googleapis.com/css2?family=Amatic+SC:wght@400;700&family=Cinzel:wght@700&family=Montserrat:wght@400;500&family=Alex+Brush&display=swap" rel="stylesheet">
<style>
  :root {
    --paper: #efebe6;
    --ink: #1f1d1b;
    --stone: #a8a5a0;
    --stone-light: #cfccc7;
  }
  * { margin: 0; padding: 0; box-sizing: border-box; }
  html, body { width: 1200px; height: 467px; overflow: hidden; background: var(--paper); }
  .label {
    position: relative;
    width: 1200px; height: 467px;
    background: var(--paper);
    color: var(--ink);
    font-family: 'Montserrat', sans-serif;
  }
  .column { position: absolute; top: 44px; font-size: 13.4px; line-height: 19px; }
  .column p { margin-bottom: 19px; }
  .column--back { left: 47px; width: 260px; }
  .column--feeding { left: 904px; width: 260px; }
  .product-type { text-decoration: underline; text-underline-offset: 2px; }
  .benefits { list-style: none; margin-bottom: 38px; }
  .benefits li::before { content: "• "; }
  .spacer-lg { height: 38px; }
  .small-print { font-size: 11px; line-height: 15.5px; margin-bottom: 15px !important; }
  .net { margin-top: 72px; }

  .brand {
    position: absolute; left: 512px; top: 88px; width: 200px;
    text-align: center; font-size: 15px; font-weight: 400; color: var(--ink);
    letter-spacing: 0.3px;
  }
  .headline {
    position: absolute; left: 380px; width: 432px; text-align: center;
    font-family: 'Amatic SC', cursive; font-weight: 400;
    font-size: 46px; line-height: 1; letter-spacing: 3px;
    text-shadow: 0 2px 3px rgba(0,0,0,0.12);
  }
  .headline--one { top: 144px; }
  .headline--two { top: 198px; }
  .highlight {
    position: absolute; left: 440px; top: 256px; width: 322px; text-align: center;
    font-family: 'Cinzel', serif; font-weight: 700; font-size: 22px; letter-spacing: 0.4px;
    text-shadow: 0 2px 3px rgba(0,0,0,0.18);
  }
  .for-dogs {
    position: absolute; left: 664px; top: 294px;
    font-family: 'Alex Brush', cursive; font-size: 34px; line-height: 1;
  }
  .paw-trail {
    position: absolute; left: 426px; top: 294px; width: 50px; height: 90px;
    background: linear-gradient(160deg, var(--stone-light), var(--stone));
    opacity: 0.45; border-radius: 6px;
  }
  .dog-sketch {
    position: absolute; left: 768px; top: 312px; width: 40px; height: 36px;
    background: var(--stone-light); opacity: 0.6; border-radius: 6px;
  }
  .natural {
    position: absolute; left: 450px; top: 392px;
    display: flex; align-items: center; gap: 14px;
  }
  .natural span { font-size: 10px; letter-spacing: 0.1px; }
</style>
</head>
<body>
<main class="label">
  <section class="column column--back">
    <p class="product-type">Ergänzungsfuttermittel für Hunde</p>
    <ul class="benefits">
      <li>trägt einer gesunden Gelenkfunktion bei</li>
      <li>zur Unterstützung des gesamten Bewegungsapparats</li>
      <li>für mehr Vitalität und Wohlbefinden</li>
    </ul>
    <div class="spacer-lg"></div>
    <p>Zusammensetzung: Brennessel, Kurkuma, Hagebutten, Leinsamen, Löwenzahn</p>
    <p>Analytische Bestandteile: Rohfaser 2,55%, Feuchtgehalt 12%</p>
  </section>

  <div class="brand">Anka's Pfotenwerk</div>
  <h1 class="headline headline--one">Nährstoffpulver</h1>
  <h2 class="headline headline--two">zur Unterstützung des</h2>
  <div class="highlight">BEWEGUNGSAPPARATS</div>
  <div class="paw-trail" role="img" aria-label="Spur aus grauen Pfotenabdrücken"></div>
  <div class="for-dogs">für Hunde</div>
  <div class="dog-sketch" role="img" aria-label="Kleine Strichzeichnung eines sitzenden Hundes"></div>
  <div class="natural">
    <svg width="44" height="44" viewBox="0 0 44 44" aria-hidden="true">
      <circle cx="22" cy="22" r="19.5" fill="none" stroke="var(--ink)" stroke-width="3"/>
      <path d="M14 30 C14 18 22 12 31 12 C31 22 25 30 14 30 Z" fill="var(--ink)"/>
      <path d="M13 32 L24 21" stroke="var(--paper)" stroke-width="1.5"/>
    </svg>
    <span>100% NATÜRLICHE INHALTSSTOFFE</span>
  </div>

  <section class="column column--feeding">
    <p>Fütterungsempfehlung:</p>
    <p>Hunde bis 20kg - 1gr täglich<br>(reicht für 6 Monate)<br>Hunde ab 20kg - 2gr täglich<br>(reicht für 3 Monate)</p>
    <p>Das Pulver kann unter dem Futter gemischt werden.</p>
    <p class="small-print net">Nettomasse: 200g</p>
    <p class="small-print">Hinweis: kühl, trocken und lichtgeschützt lagern.</p>
  </section>
</main>
</body>
</html>
```